A single page website & logo required for a Field Service Management Application

Name of the project - CrewTallo

We are software developers and we have a Field Service Management application ready. This software is all about optimizing the businesses that send their staff to various sites to provide service. Scheduling, creating jobs, quotes & invoices are a few salient features of it. It also has an accompanying Android & iPhone/iPad versions that will be used by the technicians.

More details can be provided, if needed.

After this web design project ends, the winning designer will be awarded the budget for the logo design through a 1on1 project.

Reason: I need to get the designs approved from my boss and he is currently overseas and is very busy. And hence I need the timeline to be extended.

Target Market(s)

All the Companies all over the world that send their staff to various sites to provide service.

Industry/Entity Type

Software

Logo Text

CrewTallo

Number of Pages Required

1 page

Font styles to use
Serif
Sans Serif

Requirements
Must have
• We would like to have the following components in the design:
• 1. Slider
• 2. Features of the software
• 3. Pricing Details
• 4. FAQs
• 5. Suitable for (Shows a list of all industries that our software is suitable for)
Nice to have
• A section with the background of a technician using our app on a mobile device (Screenshot can be provided)
Should not have
• Gaudy fonts and stereotypical designs

```html
<!DOCTYPE html>
<html lang="en">
<head>
<meta charset="utf-8">
<title>CrewTallo – Service Management Application</title>
<link href="https://fonts.googleapis.com/css2?family=Raleway:wght@300;400;600;700;800&family=Source+Sans+3:wght@400;600&display=swap" rel="stylesheet">
<style>
:root{
  --pink:#d42e5f;
  --ink:#333333;
  --dark:#3a3a3a;
  --text:#555555;
  --line:#dddddd;
  --soft:#f7f7f7;
  --white:#ffffff;
}
*{box-sizing:border-box;margin:0;padding:0}
html,body{width:1200px;height:2390px;overflow:hidden}
body{font-family:Arial,Helvetica,sans-serif;color:var(--ink);background:var(--white);position:relative}

/* Header */
.site-header{position:absolute;top:0;left:0;width:1200px;height:120px;background:var(--white);box-shadow:0 2px 6px rgba(0,0,0,.12);z-index:2}
.brand{position:absolute;left:100px;top:34px}
.brand-row{display:flex;align-items:center;gap:32px}
.brand-mark{width:34px;height:34px;background:var(--pink)}
.brand-name{font-family:'Raleway',sans-serif;font-weight:400;font-size:30px;letter-spacing:1px;color:var(--ink);line-height:1}
.brand-tag{font-size:13px;color:var(--ink);margin:4px 0 0 66px}
.call-us{position:absolute;right:100px;top:12px;font-family:'Raleway',sans-serif;font-size:24px;color:var(--pink)}
.call-us span{color:var(--ink)}
.main-nav{position:absolute;top:82px;left:0;width:1200px}
.main-nav a{position:absolute;font-size:14px;color:var(--ink);text-decoration:none;text-transform:uppercase}
.main-nav a.active::after{content:"";position:absolute;left:-10px;right:-10px;top:30px;height:5px;background:var(--pink)}

/* Hero */
.hero{position:absolute;top:120px;left:0;width:1200px;height:558px;
  background:linear-gradient(90deg,#d9d4d0 0%,#c9ced3 40%,#8f98a2 70%,#b9c5cf 100%)}
.hero-copy{position:absolute;left:100px;top:178px}
.hero-title{font-family:'Raleway',sans-serif;font-weight:800;font-size:54px;color:var(--pink);letter-spacing:-1px;line-height:1}
.hero-sub{margin-top:26px;font-family:'Source Sans 3',sans-serif;font-size:25px;line-height:36px;color:#3a3a3a}

/* Features */
.features{position:absolute;top:678px;left:0;width:1200px;height:412px;background:var(--pink);color:var(--white)}
.section-title{font-family:'Raleway',sans-serif;font-weight:400;font-size:30px;text-align:center;text-transform:uppercase}
.features .section-title{position:absolute;top:20px;width:100%}
.feature{position:absolute;width:300px;text-align:center}
.feature-icon{width:98px;height:98px;border-radius:50%;border:2px solid var(--white);margin:0 auto;display:flex;align-items:center;justify-content:center}
.feature-icon.filled{background:#222;border-color:#222}
.feature-name{font-family:'Source Sans 3',sans-serif;font-weight:400;font-size:27px;margin-top:14px}
.feature-text{font-size:13px;line-height:22px;margin-top:10px;padding:0 6px}
.btn-outline{display:inline-block;margin-top:18px;width:112px;height:32px;line-height:30px;border:1px solid var(--white);font-size:14px;color:var(--white);text-decoration:none}

/* Pricing */
.pricing{position:absolute;top:1090px;left:0;width:1200px;height:652px}
.pricing .section-title{position:absolute;top:44px;width:100%;color:var(--ink)}
.pricing-intro{position:absolute;top:98px;left:292px;width:616px;text-align:center;font-size:13px;line-height:22px}
.plan{position:absolute;top:188px;width:233px;height:423px;border:1px solid var(--line);background:var(--white)}
.plan-head{height:178px;background:var(--dark);color:var(--white);text-align:center;padding-top:12px;margin:-1px -1px 0}
.plan.featured .plan-head{background:var(--pink)}
.plan-name{font-family:'Raleway',sans-serif;font-size:24px;text-transform:uppercase}
.plan-price{font-family:'Raleway',sans-serif;font-weight:800;font-size:58px;line-height:66px}
.plan-desc{font-size:14px;line-height:22px;padding:0 16px}
.plan-list{list-style:none}
.plan-list li{height:40px;line-height:40px;border-bottom:1px solid var(--line);padding-left:48px;font-size:14px;color:var(--text);position:relative}
.plan-list li::before{content:"";position:absolute;left:27px;top:17px;width:7px;height:7px;border-radius:50%;background:var(--ink)}
.btn-order{display:block;width:171px;height:41px;line-height:41px;margin:19px auto 0;background:var(--pink);color:var(--white);border-radius:14px;text-align:center;font-family:'Raleway',sans-serif;font-size:24px;text-decoration:none}

/* FAQ + industries */
.info{position:absolute;top:1742px;left:0;width:1200px;height:553px;background:var(--soft)}
.info-title{position:absolute;font-family:'Raleway',sans-serif;font-weight:400;font-size:30px;text-transform:uppercase;color:var(--ink)}
.faq{position:absolute;left:104px;width:618px;background:var(--white);border:1px solid var(--line)}
.faq-q{height:46px;line-height:46px;padding:0 20px;font-size:12px;font-weight:bold;text-transform:uppercase;color:var(--ink);position:relative}
.faq-q::after{content:"+";position:absolute;right:20px;top:-2px;font-size:18px;font-weight:normal}
.faq.open .faq-q::after{content:"–"}
.faq-a{margin:0 20px;font-size:13px;line-height:22px;color:var(--text)}
.industries{position:absolute;left:786px;top:84px;list-style:none}
.industries li{height:34px;font-size:14px;color:var(--ink);display:flex;align-items:center;gap:12px}

/* Footer */
.site-footer{position:absolute;top:2295px;left:0;width:1200px;height:95px;background:var(--dark);color:var(--white)}
.footer-links{position:absolute;left:107px;top:26px;font-size:14px}
.footer-links a{color:var(--white);text-decoration:none}
.footer-links .sep{margin:0 10px}
.copyright{position:absolute;left:107px;top:52px;font-size:13px}
.footer-brand{position:absolute;right:100px;top:20px;text-align:left}
.footer-brand .brand-name{color:var(--white);font-size:28px;letter-spacing:.5px}
.footer-brand .brand-tag{color:#cccccc;margin:6px 0 0 0;font-size:13px}
</style>
</head>
<body>

<header class="site-header">
  <div class="brand">
    <div class="brand-row"><span class="brand-mark"></span><span class="brand-name">CREWTALLO</span></div>
    <div class="brand-tag">Service Management Application</div>
  </div>
  <div class="call-us">CALL US <span>+971 555 010 248</span></div>
  <nav class="main-nav">
    <a class="active" href="#" style="left:570px">Home</a>
    <a href="#" style="left:656px">Features</a>
    <a href="#" style="left:773px">Pricing Details</a>
    <a href="#" style="left:933px">FAQs</a>
    <a href="#" style="left:1015px">Contacts</a>
  </nav>
</header>

<section class="hero" role="img" aria-label="Slider photo: a businessman in a grey suit in front of a blurred city skyline">
  <div class="hero-copy">
    <h1 class="hero-title">CREWTALLO</h1>
    <p class="hero-sub">Cross-platform HTML 5/JS tools<br>for next-generation mobile<br>and web development</p>
  </div>
</section>

<section class="features">
  <h2 class="section-title">Features of the softwares</h2>
  <div class="feature" style="left:105px;top:102px">
    <div class="feature-icon filled">
      <svg width="22" height="34" viewBox="0 0 22 34" fill="none" stroke="#fff" stroke-width="2"><rect x="2" y="1" width="18" height="32" rx="3"/><line x1="2" y1="6" x2="20" y2="6"/><line x1="2" y1="27" x2="20" y2="27"/></svg>
    </div>
    <h3 class="feature-name">Serveri haldamine</h3>
    <p class="feature-text">Eu sit soluta antiopam, postea sanctus in an<br>vis. Pro primis insolens recteque ne, nos-<br>trum molestie splendide sed et elitr.</p>
    <a class="btn-outline" href="#">Learn more &gt;&gt;</a>
  </div>
  <div class="feature" style="left:430px;top:102px">
    <div class="feature-icon">
      <svg width="32" height="32" viewBox="0 0 32 32" fill="none" stroke="#fff" stroke-width="2" stroke-linejoin="round"><path d="M29 3 3 13l11 4 4 11z"/><path d="M29 3 14 17"/></svg>
    </div>
    <h3 class="feature-name">Serveri haldamine</h3>
    <p class="feature-text">Eu sit soluta antiopam, postea sanctus in an<br>vis. Pro primis insolens recteque ne, nos-<br>trum molestie splendide sed et elitr.</p>
    <a class="btn-outline" href="#">Learn more</a>
  </div>
  <div class="feature" style="left:775px;top:102px">
    <div class="feature-icon">
      <svg width="32" height="32" viewBox="0 0 32 32" fill="none" stroke="#fff" stroke-width="2"><line x1="7" y1="3" x2="7" y2="29"/><line x1="16" y1="3" x2="16" y2="29"/><line x1="25" y1="3" x2="25" y2="29"/><circle cx="7" cy="20" r="3" fill="#d42e5f"/><circle cx="16" cy="10" r="3" fill="#d42e5f"/><circle cx="25" cy="17" r="3" fill="#d42e5f"/></svg>
    </div>
    <h3 class="feature-name" style="margin-top:18px">Serveri haldamine</h3>
    <p class="feature-text">Eu sit soluta antiopam, postea sanctus in an<br>vis. Pro primis insolens recteque ne, nos-<br>trum molestie splendide sed et elitr.</p>
    <a class="btn-outline" href="#">Learn more</a>
  </div>
</section>

<section class="pricing">
  <h2 class="section-title">Pricing Details</h2>
  <p class="pricing-intro">Eu sit soluta antiopam, postea sanctus in an vis. Pro primis insolens recteque ne, nostrum mo-<br>lestie splendide sed et elitr.</p>

  <div class="plan featured" style="left:100px">
    <div class="plan-head"><div class="plan-name">Basic</div><div class="plan-price">$10</div><p class="plan-desc">Lorem avec, sant mai renas<br>sud. male vaces nor ir</p></div>
    <ul class="plan-list"><li>5 Basic Copies</li><li>Free Home Shipping</li><li>Unlimited Waranty</li><li>Unlimited Stroge</li></ul>
    <a class="btn-order" href="#">Order Now</a>
  </div>
  <div class="plan" style="left:355px">
    <div class="plan-head"><div class="plan-name">Starter</div><div class="plan-price">$60</div><p class="plan-desc">Lorem avec, sant mai renas<br>sud. male vaces nor ir</p></div>
    <ul class="plan-list"><li>5 Basic Copies</li><li>Free Home Shipping</li><li>Unlimited Waranty</li><li>Unlimited Stroge</li></ul>
    <a class="btn-order" href="#">Order Now</a>
  </div>
  <div class="plan" style="left:612px">
    <div class="plan-head"><div class="plan-name">Standard</div><div class="plan-price">$120</div><p class="plan-desc">Lorem avec, sant mai renas<br>sud. male vaces nor ir</p></div>
    <ul class="plan-list"><li>5 Basic Copies</li><li>Free Home Shipping</li><li>Unlimited Waranty</li><li>Unlimited Stroge</li></ul>
    <a class="btn-order" href="#">Order Now</a>
  </div>
  <div class="plan" style="left:867px">
    <div class="plan-head"><div class="plan-name">Professional</div><div class="plan-price">$200</div><p class="plan-desc">Lorem avec, sant mai renas<br>sud. male vaces nor ir</p></div>
    <ul class="plan-list"><li>5 Basic Copies</li><li>Free Home Shipping</li><li>Unlimited Waranty</li><li>Unlimited Stroge</li></ul>
    <a class="btn-order" href="#">Order Now</a>
  </div>
</section>

<section class="info">
  <h2 class="info-title" style="left:112px;top:26px">FAQ's</h2>
  <div class="faq open" style="top:88px;height:139px">
    <div class="faq-q">Designed for your business</div>
    <p class="faq-a">Eu sit soluta antiopam, postea sanctus in an vis. Pro primis insolens recteque ne,<br>nostrum molestie splendide sed et elitr sanctus in an vis. Pro primis insolens<br>recteque ne, nostrum molestie splendide sed et elitr.</p>
  </div>
  <div class="faq" style="top:239px"><div class="faq-q">Fully responsive</div></div>
  <div class="faq" style="top:300px"><div class="faq-q">Ample customizations</div></div>
  <div class="faq" style="top:361px"><div class="faq-q">Framework compatible</div></div>
  <div class="faq" style="top:421px"><div class="faq-q">Unique design</div></div>

  <h2 class="info-title" style="left:784px;top:26px">All industries</h2>
  <ul class="industries">
    <li><svg width="12" height="12" viewBox="0 0 12 12"><circle cx="6" cy="6" r="5" fill="none" stroke="#d42e5f" stroke-width="1.5"/><path d="M3.5 6l2 2 3-3.5" fill="none" stroke="#d42e5f" stroke-width="1.5"/></svg>Lorem ipsum dolor sit amet consectetur</li>
    <li><svg width="12" height="12" viewBox="0 0 12 12"><circle cx="6" cy="6" r="5" fill="none" stroke="#d42e5f" stroke-width="1.5"/><path d="M3.5 6l2 2 3-3.5" fill="none" stroke="#d42e5f" stroke-width="1.5"/></svg>Ut hendrerit felis molestie tincidunt turpis</li>
    <li><svg width="12" height="12" viewBox="0 0 12 12"><circle cx="6" cy="6" r="5" fill="none" stroke="#d42e5f" stroke-width="1.5"/><path d="M3.5 6l2 2 3-3.5" fill="none" stroke="#d42e5f" stroke-width="1.5"/></svg>volutpat vestibulum erat</li>
    <li><svg width="12" height="12" viewBox="0 0 12 12"><circle cx="6" cy="6" r="5" fill="none" stroke="#d42e5f" stroke-width="1.5"/><path d="M3.5 6l2 2 3-3.5" fill="none" stroke="#d42e5f" stroke-width="1.5"/></svg>Sed ornare velit eget ante fermentum</li>
    <li><svg width="12" height="12" viewBox="0 0 12 12"><circle cx="6" cy="6" r="5" fill="none" stroke="#d42e5f" stroke-width="1.5"/><path d="M3.5 6l2 2 3-3.5" fill="none" stroke="#d42e5f" stroke-width="1.5"/></svg>vitae euismod nunc semper</li>
    <li><svg width="12" height="12" viewBox="0 0 12 12"><circle cx="6" cy="6" r="5" fill="none" stroke="#d42e5f" stroke-width="1.5"/><path d="M3.5 6l2 2 3-3.5" fill="none" stroke="#d42e5f" stroke-width="1.5"/></svg>Lorem commodo interdum</li>
    <li><svg width="12" height="12" viewBox="0 0 12 12"><circle cx="6" cy="6" r="5" fill="none" stroke="#d42e5f" stroke-width="1.5"/><path d="M3.5 6l2 2 3-3.5" fill="none" stroke="#d42e5f" stroke-width="1.5"/></svg>purus ac vestibulum lorem</li>
    <li><svg width="12" height="12" viewBox="0 0 12 12"><circle cx="6" cy="6" r="5" fill="none" stroke="#d42e5f" stroke-width="1.5"/><path d="M3.5 6l2 2 3-3.5" fill="none" stroke="#d42e5f" stroke-width="1.5"/></svg>volutpat vestibulum erat</li>
    <li><svg width="12" height="12" viewBox="0 0 12 12"><circle cx="6" cy="6" r="5" fill="none" stroke="#d42e5f" stroke-width="1.5"/><path d="M3.5 6l2 2 3-3.5" fill="none" stroke="#d42e5f" stroke-width="1.5"/></svg>Sed ornare velit eget ante fermentum</li>
    <li><svg width="12" height="12" viewBox="0 0 12 12"><circle cx="6" cy="6" r="5" fill="none" stroke="#d42e5f" stroke-width="1.5"/><path d="M3.5 6l2 2 3-3.5" fill="none" stroke="#d42e5f" stroke-width="1.5"/></svg>vitae euismod nunc semper</li>
    <li><svg width="12" height="12" viewBox="0 0 12 12"><circle cx="6" cy="6" r="5" fill="none" stroke="#d42e5f" stroke-width="1.5"/><path d="M3.5 6l2 2 3-3.5" fill="none" stroke="#d42e5f" stroke-width="1.5"/></svg>Lorem commodo interdum</li>
    <li><svg width="12" height="12" viewBox="0 0 12 12"><circle cx="6" cy="6" r="5" fill="none" stroke="#d42e5f" stroke-width="1.5"/><path d="M3.5 6l2 2 3-3.5" fill="none" stroke="#d42e5f" stroke-width="1.5"/></svg>purus ac vestibulum lorem</li>
  </ul>
</section>

<footer class="site-footer">
  <nav class="footer-links">
    <a href="#">Home</a><span class="sep">|</span><a href="#">Features</a><span class="sep">|</span><a href="#">Pricing Details</a><span class="sep">|</span><a href="#">FAQs</a><span class="sep">|</span><a href="#">Contacts</a>
  </nav>
  <p class="copyright">Copyright © 2014 CrewTallo . All rights Reserved</p>
  <div class="footer-brand">
    <div class="brand-name">CREWTALLO</div>
    <div class="brand-tag">Service Management Application</div>
  </div>
</footer>

</body>
</html>
```